Looking for a modern website banner design

Bramblecrest Coaching Partners looking for the development of the main banner of the website. The project description and photos are included in the upload files.

```html
<!DOCTYPE html>
<html lang="en">
<head>
<meta charset="utf-8">
<title>Bramblecrest Coaching Partners — Banner</title>
<link href="https://fonts.googleapis.com/css2?family=Raleway:ital,wght@0,400;0,500;0,600;1,400&family=Playfair+Display:wght@700&display=swap" rel="stylesheet">
<style>
  :root{
    --white:#ffffff;
    --nav-text:#7b7f86;
    --accent:#3a9ad9;
    --brand:#1a6fc0;
    --blue-top:#0f74c4;
    --blue-mid:#0b62b0;
    --blue-deep:#0a4f96;
    --ring:rgba(255,255,255,0.06);
    --quote-mark:#2f86d6;
  }
  *{box-sizing:border-box;margin:0;padding:0}
  html,body{width:1200px;height:631px;overflow:hidden;background:var(--white);font-family:"Raleway",sans-serif}
  .banner{position:relative;width:1200px;height:631px;overflow:hidden}

  .site-header{position:absolute;top:0;left:0;width:1200px;height:69px;background:var(--white)}
  .brand{position:absolute;left:96px;top:25px;display:flex;align-items:center;gap:7px}
  .brand-dot{width:14px;height:14px;border-radius:50%;background:var(--brand)}
  .brand-name{font-size:19px;font-weight:600;color:var(--brand);letter-spacing:.5px}
  .main-nav{position:absolute;top:27px;right:103px;display:flex;gap:20px;font-size:7px;letter-spacing:1px;color:var(--nav-text);text-transform:uppercase;white-space:nowrap}
  .main-nav .nav-try{color:var(--accent)}
  .main-nav .nav-login{display:flex;align-items:center;gap:3px}
  .main-nav .nav-login svg{width:5px;height:6px}

  .hero{position:absolute;top:69px;left:0;width:654px;height:562px;overflow:hidden;
    background:radial-gradient(ellipse at 30% 15%,var(--blue-top) 0%,var(--blue-mid) 55%,var(--blue-deep) 100%)}
  .ring{position:absolute;border-radius:50%;background:var(--ring)}
  .ring-1{left:343px;top:252px;width:560px;height:560px}
  .ring-2{left:396px;top:304px;width:460px;height:460px}
  .ring-3{left:486px;top:380px;width:330px;height:330px}
  .ring-4{left:515px;top:415px;width:270px;height:270px;background:rgba(40,150,230,0.18)}

  .testimonial{position:absolute;left:97px;top:104px;width:520px;color:var(--white)}
  .quote-open{position:absolute;left:0;top:-6px;font-family:"Playfair Display",serif;font-weight:700;color:var(--quote-mark);font-size:56px;line-height:1}
  .quote-text{position:relative;margin-left:34px;width:486px;font-size:16px;line-height:24px;font-weight:400}
  .quote-close{display:inline-block;font-family:"Playfair Display",serif;font-weight:700;color:var(--quote-mark);font-size:56px;line-height:0;vertical-align:-22px;margin-left:6px}
  .author-name{margin:22px 0 0 35px;font-size:21px;font-style:italic;font-weight:400}
  .author-team{margin:6px 0 0 36px;font-size:10px;line-height:14px;font-style:italic}

  .cta{position:absolute;left:122px;top:320px;height:44px;background:var(--white);border-radius:2px;
    display:flex;align-items:center;padding:0 18px 0 10px;gap:12px;text-decoration:none;white-space:nowrap}
  .cta-dot{width:14px;height:14px;border-radius:50%;background:var(--brand)}
  .cta-label{font-size:13.5px;color:var(--brand);font-weight:500;letter-spacing:.2px}

  .hero-photo{position:absolute;top:69px;left:654px;width:546px;height:562px;
    background:linear-gradient(180deg,#3b2f2c 0%,#5a3a36 35%,#b8413c 48%,#e6e1d4 62%,#f4f6f8 100%)}
</style>
</head>
<body>
<div class="banner">
  <header class="site-header">
    <div class="brand"><span class="brand-dot"></span><span class="brand-name">Bramblecrest</span></div>
    <nav class="main-nav">
      <span>About</span>
      <span>Features</span>
      <span>Uses</span>
      <span class="nav-try">☆ Try Bramblecrest AD</span>
      <span class="nav-login"><svg viewBox="0 0 5 6"><rect x="0" y="2.5" width="5" height="3.5" fill="#7b7f86"/><path d="M1 2.5V1.6a1.5 1.5 0 0 1 3 0v.9" stroke="#7b7f86" stroke-width=".8" fill="none"/></svg>Login</span>
    </nav>
  </header>

  <section class="hero">
    <div class="ring ring-1"></div>
    <div class="ring ring-2"></div>
    <div class="ring ring-3"></div>
    <div class="ring ring-4"></div>

    <blockquote class="testimonial">
      <span class="quote-open">“</span>
      <p class="quote-text">Bramblecrest has provided support that has allowed me to develop as a person and an athlete.&nbsp; The P.A.C.E.™ process allowed me to stay focused on attainable goals each season and progress from Junior to College and now Professional Hockey.<span class="quote-close">”</span></p>
      <p class="author-name">Marcus Delane</p>
      <p class="author-team">Riverton Comets<br>Eastern Pro Hockey League</p>
    </blockquote>

    <a class="cta" href="#"><span class="cta-dot"></span><span class="cta-label">REQUEST BRAMBLECREST AD</span></a>
  </section>

  <div class="hero-photo" role="img" aria-label="Photo of a hockey player celebrating on the ice with arms raised, an opposing player skating in the foreground and a cheering crowd behind the boards"></div>
</div>
</body>
</html>
```